Restaurant needs a vertical banner for fried catfish

Our restaurant is looking for an eye-catching 78.75in. x 36in. vertical physical banner ad for our fried catfish. Photos for the fried catfish will be provided as a reference but we will also accept anything similar to the photo. We will be using the following as our receptacle: https://www.plankoria.example/banner-stand/retractable-banner-stands/
The design must incorporate the following flavor texts:
Fried Catfish
Always Fresh!
Made from Scratch
Hand-cut Fillets
The Best Catfish in Texas
Served with fries, hush puppies, and a 32oz fountain drink
Also available by the pound!
The final design should be creative, professional, and eye-catching for customers.
Updates
Colors
Designer to choose colors to be used in the design.
Requirements
Must have
- We are open to any and all design elements, albeit the 'flavor texts' should not overpower, but complement the fried catfish photo. 'Fried Catfish' can be used in lieu of a main title/logo.
Nice to have
- Transparent or textured backgrounds that can encompass any or all part of the banner such as a cutting board, shadows, abstract, etc to show depth are a plus.
- Use of vectors or objects such as ribbons or shapes to encapsulate the 'flavor texts' are also encouraged.

```html
<!DOCTYPE html>
<html lang="en">
<head>
<meta charset="utf-8">
<title>Fried Catfish – Vertical Banner</title>
<link href="https://fonts.googleapis.com/css2?family=Playball&family=Montserrat:wght@400;500;600;700;800&display=swap" rel="stylesheet">
<style>
  :root {
    --page-bg: #e4e3e3;
    --wood-light: #f1efea;
    --wood-mid: #e2dfd8;
    --ink: #1b1b1d;
    --night-top: #2c2d36;
    --night-bottom: #121319;
    --lime: #8dc63f;
    --lime-bright: #b6df5e;
    --green: #6cc04a;
    --white: #ffffff;
  }
  * { margin: 0; padding: 0; box-sizing: border-box; }
  html, body {
    width: 1200px; height: 2414px; overflow: hidden;
    background: var(--page-bg);
    font-family: "Montserrat", Arial, sans-serif;
  }
  .banner {
    position: absolute; left: 176px; top: 160px;
    width: 841px; height: 2048px; overflow: hidden;
    background: var(--night-bottom);
  }
  .tabletop-photo {
    position: absolute; left: 0; top: 0; width: 841px; height: 1000px;
    background:
      radial-gradient(ellipse 60% 30% at 50% 8%, rgba(205,60,40,.35), transparent 70%),
      linear-gradient(180deg, #e9e4d8 0%, var(--wood-light) 25%, var(--wood-mid) 100%);
  }
  .artwork { position: absolute; left: 0; top: 0; width: 841px; height: 1920px; }
  .title {
    position: absolute; left: 0; top: 222px; width: 841px;
    text-align: center;
    font-family: "Playball", cursive;
    font-size: 112px; font-weight: 400; line-height: 1;
    color: var(--ink);
  }
  .tagline {
    position: absolute; left: 140px; top: 367px; width: 557px; height: 61px;
    background: var(--lime);
    text-align: center;
    font-size: 50px; font-weight: 800; line-height: 64px; letter-spacing: -0.5px;
    color: var(--ink);
  }
  .features {
    position: absolute; left: 97px; top: 1328px; width: 520px;
    list-style: none;
  }
  .features li {
    position: relative; padding-left: 64px; margin-bottom: 16px;
    font-size: 43px; font-weight: 400; line-height: 53px; letter-spacing: 0.5px;
    color: var(--white);
  }
  .features .tick {
    position: absolute; left: 0; top: 9px; width: 36px; height: 36px;
  }
  .by-the-pound {
    position: absolute; left: 0; top: 1800px; width: 841px;
    text-align: center;
    font-size: 37px; font-weight: 600; letter-spacing: 0.5px;
    color: var(--lime);
  }
  .footer-band {
    position: absolute; left: 0; top: 1920px; width: 841px; height: 128px;
    background: linear-gradient(90deg, var(--green) 0%, var(--lime-bright) 50%, var(--green) 100%);
    text-align: center;
    font-size: 44px; font-weight: 400; line-height: 80px; letter-spacing: 0.5px;
    color: var(--ink);
  }
  .footer-band strong { font-weight: 700; }
</style>
</head>
<body>
  <main class="banner">
    <div class="tabletop-photo" role="img" aria-label="White wooden tabletop scattered with cherry tomatoes, lettuce leaves, cucumber slices and brussels sprouts"></div>

    <svg class="artwork" viewBox="0 0 841 1920" xmlns="http://www.w3.org/2000/svg">
      <defs>
        <linearGradient id="night" x1="0" y1="0" x2="0" y2="1">
          <stop offset="0" stop-color="#2c2d36"/>
          <stop offset="1" stop-color="#121319"/>
        </linearGradient>
        <radialGradient id="platter" cx="0.5" cy="0.45" r="0.6">
          <stop offset="0" stop-color="#b8741f"/>
          <stop offset="0.6" stop-color="#d9a24a"/>
          <stop offset="1" stop-color="#ecebef"/>
        </radialGradient>
        <radialGradient id="sides" cx="0.5" cy="0.4" r="0.6">
          <stop offset="0" stop-color="#e8e2c8"/>
          <stop offset="0.5" stop-color="#d4b040"/>
          <stop offset="1" stop-color="#b3783a"/>
        </radialGradient>
      </defs>

      <g role="img" aria-label="Plate of cornmeal-fried catfish fillets with french fries, hush puppies and tartar sauce">
        <ellipse cx="430" cy="860" rx="450" ry="290" fill="url(#platter)"/>
      </g>

      <path d="M0,820 C60,1000 250,1125 460,1128 C660,1130 790,1000 841,790 L841,1920 L0,1920 Z" fill="url(#night)"/>

      <path d="M0,900 C40,1010 170,1100 330,1140 C180,1120 70,1060 0,1000 Z" fill="#8dc63f"/>
      <path d="M0,1040 C120,1130 300,1160 460,1160 L500,1195 C300,1200 120,1160 0,1100 Z" fill="#8dc63f"/>
      <path d="M0,1100 C140,1170 320,1198 500,1195 L500,1215 C300,1215 120,1190 0,1150 Z" fill="#b6df5e"/>
      <path d="M730,1120 C790,1080 825,1020 841,930 L841,1120 C810,1140 770,1150 740,1155 Z" fill="#8dc63f"/>

      <g role="img" aria-label="Close-up of catfish fillets with tartar sauce, lemons and an onion">
        <circle cx="636" cy="1150" r="140" fill="url(#sides)"/>
      </g>
      <circle cx="636" cy="1150" r="140" fill="none" stroke="#6cc04a" stroke-width="16"/>
    </svg>

    <h1 class="title">Fried Catfish</h1>
    <p class="tagline">ALWAYS FRESH!</p>

    <ul class="features">
      <li><svg class="tick" viewBox="0 0 36 36"><circle cx="18" cy="18" r="18" fill="#8dc63f"/><path d="M10.5 18.5 l5 5 l10 -10" fill="none" stroke="#1b1b1d" stroke-width="3.5" stroke-linecap="round" stroke-linejoin="round"/></svg>Made from Scratch</li>
      <li><svg class="tick" viewBox="0 0 36 36"><circle cx="18" cy="18" r="18" fill="#8dc63f"/><path d="M10.5 18.5 l5 5 l10 -10" fill="none" stroke="#1b1b1d" stroke-width="3.5" stroke-linecap="round" stroke-linejoin="round"/></svg>Hand-cut Fillets</li>
      <li><svg class="tick" viewBox="0 0 36 36"><circle cx="18" cy="18" r="18" fill="#8dc63f"/><path d="M10.5 18.5 l5 5 l10 -10" fill="none" stroke="#1b1b1d" stroke-width="3.5" stroke-linecap="round" stroke-linejoin="round"/></svg>The Best Catfish in<br>Texas</li>
      <li><svg class="tick" viewBox="0 0 36 36"><circle cx="18" cy="18" r="18" fill="#8dc63f"/><path d="M10.5 18.5 l5 5 l10 -10" fill="none" stroke="#1b1b1d" stroke-width="3.5" stroke-linecap="round" stroke-linejoin="round"/></svg>Served with fries,<br>hush puppies, and a<br>32oz fountain drink</li>
    </ul>

    <p class="by-the-pound">Also available by the pound!</p>

    <footer class="footer-band">www.<strong>websitetobe</strong>.example</footer>
  </main>
</body>
</html>
```